SkyvoraQ Business Cards and Stationary Design

Need a design for our business cards and stationary. I want to carry on the theme of the logo. I want the business cards to have a design on the back. I would like the business cards and the stationary to carry the same theme, design scheme, and branding

Target Market(s)

Airlines and Maintenance Facilities

Industry/Entity Type

Aviation

Contact Information for Business Card

Name
Position Title
Address: 4827 Tollbeck Lane, Fort Pierce, Florida, 34951
Office Number
Mobile Number
Email
Website

Font styles to use
Serif
Sans Serif

Colors

Designer to choose colors to be used in the design.

```html
<!DOCTYPE html>
<html lang="en">
<head>
<meta charset="utf-8">
<title>SkyvoraQ Business Card</title>
<link href="https://fonts.googleapis.com/css2?family=Archivo:wght@500;800&family=Work+Sans:wght@400;600&display=swap" rel="stylesheet">
<style>
  :root {
    --navy: #16275a;
    --navy-deep: #0f1d48;
    --sky: #2aa3dc;
    --white: #ffffff;
    --ink: #2d3550;
    --backdrop: #e9ebf0;
  }
  * { margin: 0; padding: 0; box-sizing: border-box; }
  html, body { width: 1200px; height: 900px; overflow: hidden; }
  body {
    background: var(--backdrop);
    position: relative;
    font-family: "Work Sans", sans-serif;
  }
  .card {
    position: absolute;
    left: 285px;
    width: 630px;
    height: 360px;
    border-radius: 22px;
    overflow: hidden;
    box-shadow: 0 10px 30px rgba(15, 29, 72, 0.18);
  }
  .card-back { top: 50px; background: var(--navy); }
  .card-front { top: 490px; background: var(--white); }

  .back-pattern {
    position: absolute; inset: 0;
    background: linear-gradient(135deg, #1a2d66 0%, var(--navy) 55%, var(--navy-deep) 100%);
  }
  .back-brand {
    position: absolute;
    left: 0; right: 0; top: 150px;
    display: flex; align-items: center; justify-content: center; gap: 16px;
  }
  .back-brand .brand-name {
    font-family: "Archivo", sans-serif;
    font-weight: 800;
    font-size: 52px;
    letter-spacing: 9px;
    color: var(--white);
  }
  .back-brand .brand-dot {
    width: 50px; height: 50px; border-radius: 50%;
    border: 4px solid var(--white);
  }

  .front-waves { position: absolute; inset: 0; }

  .front-brand {
    position: absolute; left: 40px; top: 170px;
    display: flex; align-items: center; gap: 10px;
  }
  .front-brand .brand-dot {
    width: 30px; height: 30px; border-radius: 50%;
    border: 4px solid var(--navy);
  }
  .front-brand .brand-name {
    font-family: "Archivo", sans-serif;
    font-weight: 800;
    font-size: 34px;
    letter-spacing: 6px;
    color: var(--navy);
  }

  .holder {
    position: absolute; right: 40px; top: 178px; text-align: right;
  }
  .holder-name {
    font-family: "Archivo", sans-serif;
    font-weight: 500;
    font-size: 25px;
    letter-spacing: 1px;
    color: var(--navy);
  }
  .holder-title { font-size: 14px; color: var(--ink); margin-top: 2px; }

  .divider {
    position: absolute; left: 40px; right: 40px; top: 240px;
    height: 1.5px; background: var(--navy);
  }

  .contacts {
    position: absolute; left: 40px; top: 258px;
    list-style: none; font-size: 15px; color: var(--ink); line-height: 1.6;
  }
  .contacts li { display: flex; align-items: center; gap: 9px; }
  .contacts svg { width: 12px; height: 12px; fill: var(--navy); flex: none; }
  .contacts strong { font-weight: 600; color: var(--navy); }

  .address {
    position: absolute; right: 40px; top: 258px;
    text-align: right; font-size: 15px; line-height: 1.6; color: var(--ink);
    font-style: normal;
  }
</style>
</head>
<body>

<section class="card card-back">
  <div class="back-pattern" role="img" aria-label="Faint repeating brand pattern on navy"></div>
  <div class="back-brand">
    <span class="brand-name">SKYVORAQ</span>
    <span class="brand-dot"></span>
  </div>
</section>

<section class="card card-front">
  <svg class="front-waves" viewBox="0 0 630 360" preserveAspectRatio="none" aria-hidden="true">
    <rect width="630" height="360" fill="var(--white)"/>
    <path d="M0 0 H630 V40 C470 120 320 40 170 70 C90 86 30 120 0 150 Z" fill="var(--navy)"/>
    <path d="M0 150 C30 120 90 86 170 70 C250 56 300 58 360 70 C250 60 170 78 110 100 C60 118 25 140 0 170 Z" fill="var(--sky)"/>
    <path d="M170 70 C320 40 470 120 630 40 V58 C480 128 330 60 200 74 Z" fill="var(--navy-deep)"/>
  </svg>

  <div class="front-brand">
    <span class="brand-dot"></span>
    <span class="brand-name">SKYVORAQ</span>
  </div>

  <div class="holder">
    <div class="holder-name">DORIAN KELLER</div>
    <div class="holder-title">Director</div>
  </div>

  <div class="divider"></div>

  <ul class="contacts">
    <li>
      <svg viewBox="0 0 24 24"><path d="M6.6 10.8a15 15 0 0 0 6.6 6.6l2.2-2.2a1 1 0 0 1 1-.25 11.4 11.4 0 0 0 3.6.57 1 1 0 0 1 1 1V20a1 1 0 0 1-1 1A17 17 0 0 1 3 4a1 1 0 0 1 1-1h3.5a1 1 0 0 1 1 1c0 1.25.2 2.45.57 3.6a1 1 0 0 1-.25 1z"/></svg>
      513-555-0187
    </li>
    <li>
      <svg viewBox="0 0 24 24"><path d="M2 5h20v14H2z M4 7v.5l8 5 8-5V7z" fill-rule="evenodd"/></svg>
      info@skyvoraq.com
    </li>
    <li>
      <svg viewBox="0 0 24 24"><circle cx="12" cy="12" r="10"/></svg>
      <span>www.<strong>skyvoraq</strong>.com</span>
    </li>
  </ul>

  <address class="address">
    4827 Tollbeck Lane,<br>
    Fort Pierce, Florida, 34951
  </address>
</section>

</body>
</html>
```